Create banners that convert into clicks

I'm looking for a for a banner that with following details.
top slogan:
We Make Your Phone Ring.

ROI Driven SEO & PPC Campaigns.
No Hype! Just Results!

Bottom: Get A Free SEO & PPC Analysis

Image: Picture of phone off hook.
Logos and Colors Attached

Banner Sizes needed:
728x90
300x250
480x60

Reason: Not changes by designers per messages sent. would like at least 2 days.

Target Market(s)

Small To Med Size business owners

Industry/Entity Type

Seo

Requirements
Must have
• Please keep to main color scheme of logo...Blue & White.
May use a bright color to draw attention like yellow or orange or similar.

```html
<!DOCTYPE html>
<html lang="en">
<head>
<meta charset="utf-8">
<title>Brightline Marketing – Banner Set</title>
<link href="https://fonts.googleapis.com/css2?family=Open+Sans:wght@300;400;600;700&display=swap" rel="stylesheet">
<style>
  :root {
    --stage: #a86c3a;
    --navy: #0b3a78;
    --white: #ffffff;
    --brand-blue: #163f86;
    --accent-blue: #4a92e6;
    --button-blue: #2a6fd0;
    --screen-top: #5fe0bd;
    --screen-bottom: #25b08c;
    --scale: 1.232;
  }
  html, body {
    margin: 0;
    padding: 0;
    width: 1200px;
    height: 818px;
    overflow: hidden;
    background: var(--stage);
    font-family: "Open Sans", sans-serif;
  }
  .canvas {
    position: relative;
    width: 1200px;
    height: 818px;
  }
  .banner {
    position: absolute;
    background: var(--navy);
    color: var(--white);
    overflow: hidden;
    transform-origin: top left;
    transform: scale(var(--scale));
    box-shadow: 3px 3px 5px rgba(0, 0, 0, 0.45);
  }
  .banner > * { position: absolute; margin: 0; }
  .logo-panel { left: 0; top: 0; }
  .brand {
    display: flex;
    align-items: center;
    gap: 5px;
    color: var(--brand-blue);
    font-weight: 700;
    white-space: nowrap;
    line-height: 1.3;
  }
  .brand-dot {
    border-radius: 50%;
    background: var(--brand-blue);
    flex: none;
  }
  .headline { font-weight: 400; white-space: nowrap; line-height: 1.1; }
  .headline strong { font-weight: 700; }
  .subhead { color: var(--accent-blue); font-weight: 700; white-space: nowrap; line-height: 1.2; }
  .tagline { font-weight: 400; white-space: nowrap; }
  .cta {
    background: var(--button-blue);
    color: var(--white);
    font-weight: 700;
    display: flex;
    align-items: center;
    justify-content: center;
    white-space: nowrap;
  }
  .phone-art {
    border-radius: 8px;
    background: linear-gradient(135deg, #f4f4f4 0%, var(--screen-top) 25%, var(--screen-bottom) 100%);
  }

  /* 300 x 250 */
  .banner--square { left: 405px; top: 90px; width: 300px; height: 250px; }
  .banner--square .brand { left: 16px; top: 15px; font-size: 12px; }
  .banner--square .brand-dot { width: 7px; height: 7px; }
  .banner--square .headline { left: 23px; top: 56px; font-size: 22px; }
  .banner--square .subhead { left: 28px; top: 120px; font-size: 12.5px; text-align: center; }
  .banner--square .tagline { left: 23px; top: 164px; font-size: 13px; }
  .banner--square .cta { left: 10px; top: 204px; width: 277px; height: 32px; font-size: 13px; }
  .banner--square .phone-art { left: 198px; top: 32px; width: 74px; height: 142px; transform: rotate(10deg); }

  /* 728 x 90 */
  .banner--leaderboard { left: 142px; top: 453px; width: 728px; height: 90px; }
  .banner--leaderboard .brand { left: 8px; top: 14px; font-size: 12px; }
  .banner--leaderboard .brand-dot { width: 7px; height: 7px; }
  .banner--leaderboard .headline { left: 233px; top: 6px; font-size: 23px; }
  .banner--leaderboard .subhead { left: 248px; top: 35px; font-size: 13px; }
  .banner--leaderboard .tagline { left: 18px; top: 57px; font-size: 14px; }
  .banner--leaderboard .cta { left: 267px; top: 60px; width: 224px; height: 25px; font-size: 11px; }
  .banner--leaderboard .phone-art { left: 590px; top: 16px; width: 100px; height: 50px; transform: rotate(-8deg); }

  /* 470 x 60 */
  .banner--small { left: 307px; top: 612px; width: 470px; height: 60px; }
  .banner--small .brand { left: 5px; top: 8px; font-size: 7.5px; gap: 3px; }
  .banner--small .brand-dot { width: 5px; height: 5px; }
  .banner--small .headline { left: 150px; top: 2px; font-size: 14px; }
  .banner--small .subhead { left: 143px; top: 20px; font-size: 9.5px; }
  .banner--small .tagline { left: 8px; top: 38px; font-size: 10px; }
  .banner--small .cta { left: 148px; top: 37px; width: 181px; height: 19px; font-size: 8px; }
  .banner--small .phone-art { left: 370px; top: 10px; width: 72px; height: 38px; transform: rotate(-8deg); border-radius: 5px; }
</style>
</head>
<body>
<main class="canvas">

  <section class="banner banner--square" aria-label="300 by 250 banner">
    <svg class="logo-panel" width="226" height="48" viewBox="0 0 226 48" aria-hidden="true">
      <polygon points="0,0 226,0 180,48 0,48" fill="var(--white)"/>
    </svg>
    <p class="brand"><span class="brand-dot"></span>BRIGHTLINE MARKETING</p>
    <h1 class="headline">We Make Your<br>Phone <strong>Ring</strong></h1>
    <p class="subhead">ROI Driven SEO<br>&amp; PPC Campaigns.</p>
    <p class="tagline">No Hype! Just Results!</p>
    <a class="cta">Get A Free SEO &amp; PPC Analysis</a>
    <div class="phone-art" role="img" aria-label="Smartphone with a call icon on its teal screen"></div>
  </section>

  <section class="banner banner--leaderboard" aria-label="728 by 90 banner">
    <svg class="logo-panel" width="206" height="47" viewBox="0 0 206 47" aria-hidden="true">
      <polygon points="0,0 206,0 165,47 0,47" fill="var(--white)"/>
    </svg>
    <p class="brand"><span class="brand-dot"></span>BRIGHTLINE MARKETING</p>
    <h2 class="headline">We Make Your Phone <strong>Ring</strong></h2>
    <p class="subhead">ROI Driven SEO &amp; PPC Campaigns.</p>
    <p class="tagline">No Hype! Just Results!</p>
    <a class="cta">Get A Free SEO &amp; PPC Analysis</a>
    <div class="phone-art" role="img" aria-label="Smartphone lying sideways with a call icon on its teal screen"></div>
  </section>

  <section class="banner banner--small" aria-label="480 by 60 banner">
    <svg class="logo-panel" width="132" height="30" viewBox="0 0 132 30" aria-hidden="true">
      <polygon points="0,0 132,0 108,30 0,30" fill="var(--white)"/>
    </svg>
    <p class="brand"><span class="brand-dot"></span>BRIGHTLINE MARKETING</p>
    <h3 class="headline">We Make Your Phone <strong>Ring</strong></h3>
    <p class="subhead">ROI Driven SEO &amp; PPC Campaigns.</p>
    <p class="tagline">No Hype! Just Results!</p>
    <a class="cta">Get A Free SEO &amp; PPC Analysis</a>
    <div class="phone-art" role="img" aria-label="Smartphone lying sideways with a call icon on its teal screen"></div>
  </section>

</main>
</body>
</html>
```